We need a website for an ice cream shop "otter ice cream"

We are opening an ice cream shop called "otter ice cream". We already have a logo (photo attached). The ice cream shop will be in the style of "Harbor Neon" movie - palm trees, sunset, there will be a flamingo on the wall, so basically sunset, beach, Miami style. We would like the website to be colorful, colors of sunset, colorful buildings, girls wearing vintage roller skates. You can get inspiration from the "Harbor Neon" movie. We would like the website to be playful, a little vintage, not boring. The website should attract people's attention.

Target Market(s)

everyone

Industry/Entity Type

ice cream shop

Number of Pages Required

5+ page

Font styles to use
Sans Serif
Script

Colors
0094D4
00A9DD
6FCCEA
C7EBF8
E9F6FB
FFC000
F8CF3A
FAE287
FDF2CF
FEFAEE
F0912C
F2A743
F7CA91
FBE8D2
FDF5EE
EE7325
F08F49
F5BC92
FAE3D3
FDF4ED
E54698
E96AAD
F1A4CE
F9D9EA
FCEFF6
A7469A
B969AE
D3A5CF
EDDBEB
F8F0F9

Requirements
Must have
• tropical, Miami style, sunset
Nice to have
• palm trees, flamingo, girls on vintage roller skates, sea, colorful buildings

```html
<!DOCTYPE html>
<html lang="en">
<head>
<meta charset="utf-8">
<title>Otter Ice Creams</title>
<link rel="stylesheet" href="https://fonts.googleapis.com/css2?family=DM+Serif+Display&family=Nunito:wght@400;600;700&family=Lobster+Two:wght@400;700&display=swap">
<style>
:root{
  --ink:#2b2523;
  --text:#5a5552;
  --orange:#f0912c;
  --orange-soft:#f2a743;
  --peach:#f7ca91;
  --page:#ffffff;
  --gallery:#f3f3f1;
  --sky-top:#c6466f;
  --sky-mid:#ef7a5c;
  --sky-low:#f29069;
  --sea:#ee6a6f;
}
*{box-sizing:border-box;margin:0;padding:0}
html,body{width:1200px;height:2805px;overflow:hidden;background:var(--page)}
body{position:relative;font-family:"Nunito",sans-serif;color:var(--ink)}

.site-nav{position:absolute;left:0;top:0;width:1200px;height:80px;background:#f5f4f2;border-radius:0 0 64px 64px;z-index:3;display:flex;align-items:center;padding:0 40px}
.brand{display:flex;align-items:center;gap:10px;font:700 15px "Nunito",sans-serif;color:var(--ink)}
.brand-dot{width:22px;height:22px;border-radius:50%;background:var(--orange)}
.nav-links{position:absolute;left:685px;top:30px;display:flex;gap:42px;list-style:none}
.nav-links a{font:700 13px "Nunito",sans-serif;color:#3b3532;text-decoration:none}

.hero{position:absolute;left:0;top:0;width:1200px;height:664px;overflow:hidden}
.hero-scene{position:absolute;inset:0;background:linear-gradient(180deg,var(--sky-top) 0%,#dd5f67 22%,var(--sky-mid) 45%,var(--sky-low) 62%,#e45f76 72%,var(--sea) 100%)}
.hero-wave{position:absolute;left:0;bottom:0;width:1200px;height:70px}
.hero-title{position:absolute;left:0;width:1200px;top:205px;text-align:center;font:400 58px "DM Serif Display",serif;color:#fff;text-shadow:2px 2px 0 #5a2a2a}
.hero-sub{position:absolute;left:260px;width:680px;top:288px;text-align:center;font:600 19px/28px "Nunito",sans-serif;color:#fff}
.hero-btn{position:absolute;left:481px;top:368px;width:240px;height:52px;border:2px solid #3a2018;border-radius:26px;background:var(--orange-soft);box-shadow:0 0 12px rgba(255,230,200,.7);font:700 21px/48px "Lobster Two",sans-serif;color:#2b1a12;text-align:center;text-decoration:none}

.section-icon{position:absolute;left:580px;width:40px;height:52px}
.section-title{position:absolute;left:0;width:1200px;text-align:center;font:400 52px "DM Serif Display",serif;color:var(--ink);text-shadow:2px 2px 0 var(--peach)}
.section-rule{position:absolute;left:567px;width:66px;height:2px;background:#ddd}

.about-heading{position:absolute;left:125px;top:940px;font:400 33px "DM Serif Display",serif;color:var(--ink)}
.about-text{position:absolute;left:125px;width:545px;font:400 12.5px/23px "Nunito",sans-serif;color:var(--text)}
.perks{position:absolute;left:125px;top:1150px;list-style:none}
.perks li{display:flex;align-items:center;gap:10px;height:26.7px;font:700 13px "Nunito",sans-serif;color:#4a4542}
.perks svg{width:16px;height:16px}
.about-photo{position:absolute;left:694px;top:942px;width:381px;height:332px;border-radius:12px;background:radial-gradient(ellipse at 50% 55%,#6b3c34 0%,#8d5a52 40%,#b58277 75%,#c9958a 100%)}
.dots{position:absolute;left:858px;top:1292px;display:flex;gap:9px}
.dots span{width:11px;height:11px;border-radius:50%;border:1.5px solid #bbb}
.dots span.on{background:var(--orange);border-color:var(--orange)}

.gallery{position:absolute;left:0;top:1364px;width:1200px;height:1441px;background:var(--gallery)}
.gallery-band{position:absolute;left:0;top:0;width:1200px;height:90px;background:linear-gradient(180deg,#ecebe8,var(--gallery))}
.polaroid{position:absolute;width:230px;background:#fff;padding:24px 22px 0;box-shadow:0 4px 12px rgba(0,0,0,.12)}
.polaroid .shot{width:186px;height:186px}
.polaroid p{height:80px;display:flex;align-items:center;justify-content:center;text-align:center;font:400 17px/19px "Lobster Two",sans-serif;color:#2b2523}
.tilt-r{transform:rotate(5deg)}
.tilt-l{transform:rotate(-5deg)}
</style>
</head>
<body>

<header class="site-nav">
  <div class="brand"><span class="brand-dot"></span>Otter Ice Cream</div>
  <ul class="nav-links">
    <li><a href="#">Home</a></li>
    <li><a href="#">About</a></li>
    <li><a href="#">Services</a></li>
    <li><a href="#">Menu</a></li>
    <li><a href="#">Contact</a></li>
  </ul>
</header>

<section class="hero">
  <div class="hero-scene" role="img" aria-label="Sunset beach illustration with palm trees, mountains and sea"></div>
  <h1 class="hero-title">Welcome to Otter Ice creams</h1>
  <p class="hero-sub">We have over 300 delicious flavours for you to choose, come and visit our shop today!</p>
  <a class="hero-btn" href="#">Contact Us</a>
  <svg class="hero-wave" viewBox="0 0 1200 70" preserveAspectRatio="none"><path d="M0 70 C200 20 350 0 480 0 C700 0 950 20 1200 64 L1200 70 Z" fill="#fff"/></svg>
</section>

<svg class="section-icon" style="top:714px" viewBox="0 0 40 52" fill="none" stroke="#f5bc92" stroke-width="2"><path d="M6 26h28l-5 24H11z"/><path d="M14 26l2 24M20 26v24M26 26l-2 24"/><path d="M5 26c0-6 4-9 8-9 1-5 5-8 9-8 5 0 9 4 9 9 3 1 5 4 4 8"/><circle cx="24" cy="5" r="3"/></svg>
<h2 class="section-title" style="top:786px">About Us</h2>
<div class="section-rule" style="top:874px"></div>

<h3 class="about-heading">Delicious Ice Creams</h3>
<p class="about-text" style="top:996px">Placerat a ultricies a, posuere a nibh. Fusce mollis imperdiet interdum donec eget metus auguen unc vel mauris ultricies, vest ibulum orci eget,Fusce mollis imperdiet interdum donec eget metus auguen unc vel lorem ispuet.</p>
<p class="about-text" style="top:1072px">Placerat a ultricies a, posuere a nibh lorem ispuet Ibu lum orci eget.Ibu lum orci eget, viverra elit liquam erat volut pat phas ellus ac sodales Lorem ipsum dolor sit amet, consectetur adipisicing elit uasi quidem minus id omnis.</p>
<ul class="perks">
  <li><svg viewBox="0 0 16 16"><path d="M2 8c0-3 3-5 6-5s6 2 6 5z" fill="#f0912c"/><path d="M3 9h10l-2 6H5z" fill="#f2a743"/></svg>We are a family owned Business</li>
  <li><svg viewBox="0 0 16 16"><path d="M2 8c0-3 3-5 6-5s6 2 6 5z" fill="#f0912c"/><path d="M3 9h10l-2 6H5z" fill="#f2a743"/></svg>Vegan and Gluten free options always available</li>
  <li><svg viewBox="0 0 16 16"><path d="M2 8c0-3 3-5 6-5s6 2 6 5z" fill="#f0912c"/><path d="M3 9h10l-2 6H5z" fill="#f2a743"/></svg>We use high quality fair trade Chocolate in our products</li>
  <li><svg viewBox="0 0 16 16"><path d="M2 8c0-3 3-5 6-5s6 2 6 5z" fill="#f0912c"/><path d="M3 9h10l-2 6H5z" fill="#f2a743"/></svg>You can order your own custom Ice cream with us</li>
</ul>
<div class="about-photo" role="img" aria-label="Photo of a chocolate ice cream cone with sprinkles at a seaside promenade"></div>
<div class="dots"><span></span><span></span><span class="on"></span></div>

<section class="gallery">
  <div class="gallery-band"></div>
</section>
<svg class="section-icon" style="top:1414px" viewBox="0 0 40 52" fill="none" stroke="#f5bc92" stroke-width="2"><path d="M6 26h28l-5 24H11z"/><path d="M14 26l2 24M20 26v24M26 26l-2 24"/><path d="M5 26c0-6 4-9 8-9 1-5 5-8 9-8 5 0 9 4 9 9 3 1 5 4 4 8"/><circle cx="24" cy="5" r="3"/></svg>
<h2 class="section-title" style="top:1484px">Our Gallery</h2>
<div class="section-rule" style="top:1573px"></div>

<figure class="polaroid tilt-r" style="left:141px;top:1660px"><div class="shot" role="img" aria-label="Photo of pink frosted cupcakes" style="background:linear-gradient(135deg,#e7d8d2,#c45a86,#f0c6cf)"></div><p>Delicious Cupcakes</p></figure>
<figure class="polaroid tilt-l" style="left:370px;top:1714px"><div class="shot" role="img" aria-label="Photo of cream tarts with cherries" style="background:linear-gradient(135deg,#f3ece4,#e2a85a,#f7efe6)"></div><p>Our famous Petit four</p></figure>
<figure class="polaroid tilt-r" style="left:598px;top:1660px"><div class="shot" role="img" aria-label="Photo of birthday cupcakes with blue frosting" style="background:linear-gradient(135deg,#f0c8cc,#7fc9d4,#b98a62)"></div><p>Birthday Cupcakes</p></figure>
<figure class="polaroid tilt-l" style="left:828px;top:1714px"><div class="shot" role="img" aria-label="Photo of a layered cake slice with red berries" style="background:linear-gradient(135deg,#2c4766,#f1e3c4,#b5303a)"></div><p>Classic Xmas Ice Cream</p></figure>

<figure class="polaroid tilt-r" style="left:141px;top:2016px"><div class="shot" role="img" aria-label="Photo of a tiered wedding cake with red roses" style="background:linear-gradient(135deg,#e9eaea,#d7c39a,#c23a3a)"></div><p>Wedding Ice Cream</p></figure>
<figure class="polaroid tilt-l" style="left:370px;top:2070px"><div class="shot" role="img" aria-label="Photo of a berry fruit cake slice" style="background:linear-gradient(180deg,#c72a3c,#f2eee8,#5a3020)"></div><p>Our popular Fruit cake</p></figure>
<figure class="polaroid tilt-r" style="left:598px;top:2016px"><div class="shot" role="img" aria-label="Photo of hands decorating a chocolate drip cake" style="background:linear-gradient(135deg,#f3e6e6,#4a2a22,#e8a0b0)"></div><p>Finishing a cake for a Birthday</p></figure>
<figure class="polaroid tilt-l" style="left:828px;top:2070px"><div class="shot" role="img" aria-label="Photo of colourful ice cream cake pops" style="background:linear-gradient(135deg,#e4e0dc,#f2c64a,#e86a7a)"></div><p>Ice Cream pops for a birthday</p></figure>

<figure class="polaroid tilt-r" style="left:141px;top:2372px"><div class="shot" role="img" aria-label="Photo of a cheesecake slice with cherry topping" style="background:linear-gradient(180deg,#b4232e,#f4e5c8,#e9d7b2)"></div><p>Classic NY Cheesecake</p></figure>
<figure class="polaroid tilt-l" style="left:370px;top:2426px"><div class="shot" role="img" aria-label="Photo of a pink drip birthday cake" style="background:linear-gradient(135deg,#dcd9d6,#f0bccb,#f7f2ef)"></div><p>Birthday Ice Cream</p></figure>
<figure class="polaroid tilt-r" style="left:598px;top:2372px"><div class="shot" role="img" aria-label="Photo of a brownie with vanilla ice cream" style="background:linear-gradient(135deg,#f4f0ea,#f2e6cc,#4e2c1e)"></div><p>Brownie and ice cream</p></figure>
<figure class="polaroid tilt-l" style="left:828px;top:2426px"><div class="shot" role="img" aria-label="Photo of mini cream tarts topped with cherries" style="background:linear-gradient(135deg,#f3ece4,#e2a85a,#f7efe6)"></div><p>Mini cream tarts with cherry</p></figure>

</body>
</html>
```